Honey Bottle Labels for Honey Business

The honey is a niche product and the logo should exude a strong impression of wild and raw honey and natural – as in natural beekeeping. We try to keep things as simple as possible; this includes the processes the honey goes through.
We are looking for something with a gourmet / classy upmarket look and feel design. For example: Ideas with bees, honeycomb, modern or hexagonal feature; something eye catching, but not too busy.
Our honey is all natural and organic. We are a clean, simple yet sophisticated business, so would like our logo to reflect these principles.

Feel free to expand your creativity to anything you may think would look awesome and original!

The label needs to contain:
1. Our company logo. (Please see attached)
2. 100% Pure Raw Honey / Local
3. Net Wt: 16 oz (454 g) (this is the weight of the honey and will need to be modified based on bottle size.)
4. Address, Birch Hollow, MN 56000 (not larger than 1/16th inch)

Needs to be versatile to include possibility of clear label, I have included some example pictures as ideas (oval, round, square tags)

Sizes needed:
Large oval 2 5/8" x 4 1/2"
Small oval: 1 3/4" wide x 3" tall
Rectangle 1 3/4" tall x 5" wide
Round diameter 2.5"

Target Market(s)

Gourmet stores, market stall, local tourist market, potential store door sales

Requirements
Must have
• - A design that can be used on various packaging, jars and containers. We are hoping to scale up the production and want something to suit.
• - has to have a wow to stand out on the supermarket shelves
Nice to have
• Things we like:
• Minimalist designs
• Clever designs
• We don't like hand drawn font types
• We are open to the use of a hexagon in the logo, but not must have
Should not have
• Things we do not like:
• Too many colors

```html
<!DOCTYPE html>
<html lang="en">
<head>
<meta charset="utf-8">
<title>Raw Honey Jar Label</title>
<link href="https://fonts.googleapis.com/css2?family=Lato:ital,wght@0,400;0,700;0,900;1,400&display=swap" rel="stylesheet">
<style>
  :root {
    --backdrop: #e6ca3f;
    --label-white: #f4f2ee;
    --comb-amber: #eec79a;
    --brand-brown: #5a3416;
    --honey-orange: #e8901c;
    --ink: #3a2a1c;
    --rule-grey: #a9a6a2;
  }
  * { box-sizing: border-box; margin: 0; padding: 0; }
  html, body {
    width: 1070px;
    height: 1200px;
    overflow: hidden;
    background: var(--backdrop);
    font-family: "Lato", Arial, sans-serif;
  }
  .label {
    position: absolute;
    left: 85px;
    top: 205px;
    width: 900px;
    height: 790px;
    background: var(--label-white);
    overflow: hidden;
  }
  .comb-field {
    position: absolute;
    left: 0; top: 0;
    width: 100%;
    height: 360px;
    background: linear-gradient(180deg, var(--comb-amber) 0%, rgba(238,199,154,0.45) 55%, rgba(244,242,238,0) 100%);
  }
  .brand-tab {
    position: absolute;
    left: 285px;
    top: 0;
    width: 330px;
    height: 345px;
    background: var(--brand-brown);
    border-radius: 0 0 165px 165px;
  }
  .brand-name {
    position: absolute;
    left: 0; right: 0;
    top: 180px;
    text-align: center;
    color: var(--label-white);
    font-weight: 700;
    font-size: 28px;
    line-height: 1;
    white-space: nowrap;
  }
  .rule {
    position: absolute;
    left: 180px;
    width: 540px;
    border-top: 3px dashed var(--rule-grey);
  }
  .rule--top { top: 378px; }
  .rule--bottom { top: 578px; }
  .claim {
    position: absolute;
    left: 0; right: 0;
    text-align: center;
    color: var(--honey-orange);
    white-space: nowrap;
  }
  .claim--pure {
    top: 402px;
    font-weight: 900;
    font-size: 92px;
    letter-spacing: -4px;
    line-height: 1;
  }
  .claim--raw {
    top: 505px;
    font-weight: 700;
    font-size: 42px;
    line-height: 1;
  }
  .net-weight {
    position: absolute;
    left: 0; right: 0;
    top: 612px;
    text-align: center;
    color: var(--ink);
    font-weight: 700;
    font-size: 30px;
  }
  .base-band {
    position: absolute;
    left: 0; bottom: 0;
    width: 100%;
    height: 100px;
  }
  .address {
    position: absolute;
    left: 0; right: 0;
    bottom: 22px;
    text-align: center;
    color: #ffffff;
    font-style: italic;
    font-size: 27px;
  }
</style>
</head>
<body>
  <main class="label">
    <div class="comb-field" role="img" aria-label="Soft honeycomb hexagon pattern fading from amber to white"></div>

    <div class="brand-tab">
      <div class="brand-name">meadowlark honey</div>
    </div>

    <div class="rule rule--top"></div>
    <h1 class="claim claim--pure">100% PURE</h1>
    <p class="claim claim--raw">RAW HONEY/LOCAL</p>
    <div class="rule rule--bottom"></div>

    <p class="net-weight">Net Wt: 16 oz (454 g)</p>

    <svg class="base-band" viewBox="0 0 900 100" preserveAspectRatio="none" aria-hidden="true">
      <path d="M0 100 L0 45 Q450 -25 900 45 L900 100 Z" fill="#5a3416"/>
      <path d="M0 40 Q450 -32 900 40" fill="none" stroke="#c9c6c2" stroke-width="4"/>
    </svg>
    <p class="address">Birch Hollow, MN 56000</p>
  </main>
</body>
</html>
```